National Conference Logo and Website Banner

We need a National Conference Graphic in two sizes/orientations for our upcoming National Conference. This is not the logo for the association. We already have a logo for the association. See the attachment for an example of last year's national conference graphic image.

One of the images will be used un an 8.5 x 11 orientation for the cover of our Event Cover and also be used as the image on a 5.5" x 8.5" mailed post card.

The other image needs to be 2000 x 685 pixels and will be used as a header across the top of our website.

We already have a background picture we want to use (sail boats in San Deigo Harbor) and a theme (Chart Your Course to Success). But, we need to be able to incorporate our Association Brand which is missing from this Save the Date. Logo variations attached. I would like to see two logo variations. One using the color logo and the other using the white or black logo.

The theme of the Conference is "Chart Your Course for Success". The date of the conference is February 11-13, 2019 and the location is San Diego, CA. These elements should be present in the design.

Our Brand Font is Avenir but I am open to using an alternative font. I have also attached a logo color palatte.

You can get a better feel for our organization at www.lanternpathgroup.org

Target Market(s)

Non-profit leaders, superintendents and board members.

Industry/Entity Type

Non Profit

Font styles to use
Serif
Sans Serif

Colors
ffc214
1e65ad

Requirements
Must have
• One of the images will be used un an 8.5 x 11 orientation for the cover of our Event Cover and also be used as the image on a 5.5" x 8.5" mailed post card.
• The other image needs to be 2000 x 685 pixels and will be used as a header across the top of our website.
• We already have a background picture we want to use and a theme (attached). But, we need to be able to incorporate our Association Brand which is missing from this Save the Date. Logo variations attached.
• The theme of the Conference is "Chart Your Course for Success". The date of the conference is February 11-13, 2019 and the location is San Diego, CA. These elements should be present in the design.
Nice to have
• I would like to see two logo variations. One using the color logo and the other using the white or black logo.
Should not have
• Anything cutesy. While we serve education foundations, there is nothing cute or child like about our brand.

```html
<!DOCTYPE html>
<html lang="en">
<head>
<meta charset="utf-8">
<title>2019 LPG National Conference – Banner</title>
<link rel="stylesheet" href="https://fonts.googleapis.com/css2?family=Nunito+Sans:wght@300;400;600;700;800&display=swap">
<style>
  :root {
    --page-bg: #ffffff;
    --brand-blue: #24408e;
    --text-white: #ffffff;
    --sky-top: #5f7790;
    --sky-haze: #9aa7b3;
    --water-top: #3a5166;
    --water-deep: #1b2c3c;
    --rule-white: rgba(255, 255, 255, 0.75);
  }
  html, body {
    margin: 0;
    padding: 0;
    width: 1200px;
    height: 999px;
    overflow: hidden;
    background: var(--page-bg);
    font-family: "Nunito Sans", "Avenir", sans-serif;
  }
  .canvas {
    position: relative;
    width: 1200px;
    height: 999px;
  }
  .banner {
    position: absolute;
    left: 51px;
    top: 311px;
    width: 1100px;
    height: 377px;
    overflow: hidden;
  }
  .banner-photo {
    position: absolute;
    inset: 0;
    background: linear-gradient(180deg,
      var(--sky-top) 0%,
      #7d92a6 40%,
      var(--sky-haze) 70%,
      var(--water-top) 76%,
      var(--water-deep) 100%);
  }
  .brand {
    position: absolute;
    left: 27px;
    top: 36px;
    width: 322px;
  }
  .brand-name {
    display: flex;
    align-items: center;
    gap: 12px;
    color: var(--brand-blue);
    font-weight: 700;
    font-size: 31px;
    line-height: 1;
    letter-spacing: 0.5px;
    padding-bottom: 14px;
  }
  .brand-mark {
    width: 26px;
    height: 26px;
    background: var(--brand-blue);
    flex: none;
  }
  .brand-rule {
    height: 2px;
    background: var(--brand-blue);
  }
  .brand-url {
    margin-top: 6px;
    text-align: right;
    color: var(--brand-blue);
    font-size: 10px;
    font-weight: 400;
  }
  .headline {
    position: absolute;
    left: 25px;
    top: 151px;
    margin: 0;
    color: var(--text-white);
    font-weight: 600;
    font-size: 55px;
    line-height: 1;
    letter-spacing: 1px;
    text-shadow: 2px 2px 4px rgba(0, 0, 0, 0.45);
    white-space: nowrap;
  }
  .theme {
    position: absolute;
    left: 26px;
    top: 229px;
    margin: 0;
    color: var(--text-white);
    font-weight: 800;
    font-size: 35px;
    line-height: 1;
    letter-spacing: 0.5px;
    text-shadow: 2px 2px 4px rgba(0, 0, 0, 0.5);
    white-space: nowrap;
  }
  .date-rule {
    position: absolute;
    left: 26px;
    top: 304px;
    width: 358px;
    height: 1px;
    background: var(--rule-white);
  }
  .event-details {
    position: absolute;
    left: 26px;
    top: 317px;
    margin: 0;
    color: var(--text-white);
    font-weight: 300;
    font-size: 22px;
    line-height: 1.1;
    white-space: nowrap;
  }
</style>
</head>
<body>
  <main class="canvas">
    <section class="banner">
      <div class="banner-photo" role="img" aria-label="Photograph of a tall-masted schooner under white sails in San Diego Harbor, with a fleet of small sailboats and the city skyline behind"></div>

      <div class="brand">
        <div class="brand-name"><span class="brand-mark"></span>Lantern Path Group</div>
        <div class="brand-rule"></div>
        <div class="brand-url">www.lanternpathgroup.org</div>
      </div>

      <h1 class="headline">2019 LPG NATIONAL CONFERENCE</h1>
      <h2 class="theme">CHART YOUR COURSE FOR SUCCESS</h2>
      <div class="date-rule"></div>
      <p class="event-details">February 11-13 San Diego, CA.</p>
    </section>
  </main>
</body>
</html>
```